Need Business Card for our Indian Grocery Store

Industry/Entity Type

Grocery Store

Contact Information for Business Card

Manoj Varkey
Director

Store Locations:

Kelverton
482 Fenwick Road
P: 03 9581 2046

Brookvale
613 Larchmont
P: 03 9572 8814

email: pvtstores@mailbrook.net

Requirements
Must have
• Our logo Colours

```html
<!DOCTYPE html>
<html lang="en">
<head>
<meta charset="UTF-8">
<title>PVT Groceries &amp; Spices – Business Card</title>
<link rel="stylesheet" href="https://fonts.googleapis.com/css2?family=Montserrat:wght@400;600&display=swap">
<style>
  :root {
    --brand-red: #d71b24;
    --card-white: #f4f4f4;
    --stage-grey: #e4e5e7;
    --text-light: #ffffff;
    --pattern-red: #cf1921;
    --pattern-white: #efefef;
  }
  * { margin: 0; padding: 0; box-sizing: border-box; }
  html, body {
    width: 1200px;
    height: 800px;
    overflow: hidden;
    background: var(--stage-grey);
    font-family: "Montserrat", sans-serif;
  }
  .sheet {
    width: 1200px;
    height: 800px;
    display: flex;
    align-items: center;
    justify-content: center;
    gap: 60px;
  }
  .card {
    position: relative;
    width: 504px;
    height: 288px;
    overflow: hidden;
    box-shadow: 0 6px 18px rgba(0, 0, 0, 0.12);
  }
  .card-pattern {
    position: absolute;
    inset: 0;
  }
  .card--front { background: var(--card-white); }
  .card--front .card-pattern { background: var(--pattern-white); }
  .card--back { background: var(--brand-red); }
  .card--back .card-pattern { background: var(--pattern-red); }

  .brand-name {
    position: absolute;
    inset: 0;
    display: flex;
    align-items: center;
    justify-content: center;
    color: var(--brand-red);
    font-weight: 600;
    font-size: 26px;
    letter-spacing: 0.5px;
  }

  .contact {
    position: absolute;
    left: 48px;
    top: 78px;
    color: var(--text-light);
    font-size: 15px;
    line-height: 1.62;
    list-style: none;
  }
  .contact-name { font-weight: 600; }
  .contact-role { font-weight: 400; }
  .contact-line {
    display: flex;
    align-items: center;
    gap: 8px;
    white-space: nowrap;
  }
  .contact-icon {
    width: 13px;
    height: 13px;
    flex: none;
  }
</style>
</head>
<body>
<main class="sheet">
  <section class="card card--front">
    <div class="card-pattern" role="img" aria-label="Faint geometric cube pattern"></div>
    <div class="brand-name">PVT Groceries &amp; Spices</div>
  </section>

  <section class="card card--back">
    <div class="card-pattern" role="img" aria-label="Faint geometric cube pattern"></div>
    <ul class="contact">
      <li class="contact-line"><span><span class="contact-name">Manoj Varkey</span> <span class="contact-role">Director</span></span></li>
      <li class="contact-line">Kelverton, 482 Fenwick Road</li>
      <li class="contact-line">
        <svg class="contact-icon" viewBox="0 0 16 16" aria-hidden="true"><circle cx="8" cy="8" r="7" fill="none" stroke="#fff" stroke-width="1.5"/><path d="M5.5 4.5l1.5 1.5-1 1c.6 1.2 1.5 2.1 2.7 2.7l1-1 1.5 1.5-1.2 1.2C7.5 11 5 8.5 4.3 5.7z" fill="#fff"/></svg>
        <span>03 9581 2046</span>
      </li>
      <li class="contact-line">Brookvale : 613 Larchmont</li>
      <li class="contact-line">
        <svg class="contact-icon" viewBox="0 0 16 16" aria-hidden="true"><circle cx="8" cy="8" r="7" fill="none" stroke="#fff" stroke-width="1.5"/><path d="M5.5 4.5l1.5 1.5-1 1c.6 1.2 1.5 2.1 2.7 2.7l1-1 1.5 1.5-1.2 1.2C7.5 11 5 8.5 4.3 5.7z" fill="#fff"/></svg>
        <span>03 9572 8814</span>
      </li>
      <li class="contact-line">
        <svg class="contact-icon" viewBox="0 0 16 16" aria-hidden="true"><rect x="1" y="3" width="14" height="10" fill="none" stroke="#fff" stroke-width="1.5"/><path d="M1 3l7 6 7-6M1 13l5-5M15 13l-5-5" fill="none" stroke="#fff" stroke-width="1.3"/></svg>
        <span>pvtstores@mailbrook.net</span>
      </li>
    </ul>
  </section>
</main>
</body>
</html>
```